7th Annual Falcon Ridge Classic Flyer

Looking to design an updated eye catching flyer maybe with someone movement, sound, and color. Below is an attachment of the flyer I have used in the past. I need to add color, sound, and movement to the flyer. This is an advertisement for youth folk style wrestling. You may contact me directly at 252-381-4927 if you need additional information. I really like the colors music and movement in the video below.
https://www.vidloomer.com/watch?v=kQ7mTbLw2Ra

Target Market(s)

Youth Wrestling

Font styles to use
Serif

Colors
EB3D1F
EC4F4E
F09395
F8D3D4
FCEDEE

Requirements
Must have
• All information included on flyer.
Nice to have
• Color, sound, and movement

```html
<!DOCTYPE html>
<html lang="en">
<head>
<meta charset="utf-8">
<title>7th Annual Falcon Ridge Classic</title>
<link rel="stylesheet" href="https://fonts.googleapis.com/css2?family=Archivo+Black&family=Poppins:ital,wght@0,500;0,600;1,300;1,400&display=swap">
<style>
  :root {
    --page: #f3efef;
    --flyer-deep: #5e0f0d;
    --flyer-mid: #a3231c;
    --flyer-hot: #c8342a;
    --label-red: #e42a2a;
    --panel-dark: rgba(38, 8, 8, 0.72);
    --text-light: #f7ecec;
    --rule-light: #f4e4e4;
    --title-stroke: #e0262a;
    --title-shadow: #1a0505;
    --art-dark: #2a1413;
    --art-mid: #4a1e1b;
  }
  * { margin: 0; padding: 0; box-sizing: border-box; }
  html, body { width: 927px; height: 1200px; overflow: hidden; }
  body { background: var(--page); position: relative; font-family: "Poppins", sans-serif; color: var(--text-light); }

  .flyer {
    position: absolute; left: 71px; top: 46px; width: 784px; height: 1108px; overflow: hidden;
    background: radial-gradient(ellipse at 55% 55%, var(--flyer-hot) 0%, var(--flyer-mid) 45%, var(--flyer-deep) 100%);
  }
  .flyer-texture {
    position: absolute; inset: 0;
    background: radial-gradient(ellipse 38% 48% at 50% 56%, rgba(220,70,60,0.35), rgba(0,0,0,0) 70%);
  }
  .abs { position: absolute; }

  .title { left: 70px; top: 32px; font-family: "Archivo Black", sans-serif; color: #fbeaea;
    -webkit-text-stroke: 1.4px var(--title-stroke); text-shadow: 3px 3px 0 var(--title-shadow); }
  .title-num { position: absolute; left: 0; top: 0; font-size: 84px; line-height: 80px; font-style: italic; }
  .title-sup { position: absolute; left: 50px; top: 2px; font-size: 17px; line-height: 20px; -webkit-text-stroke: 0; color: #fff; }
  .title-name { position: absolute; left: 47px; top: 26px; font-size: 34px; line-height: 42px; white-space: nowrap; letter-spacing: -0.6px; }

  .label { background: var(--label-red); color: #fff; font-weight: 600; font-size: 13.5px; line-height: 16px; padding: 0 5px; }
  .label-wide { width: 126px; height: 23px; line-height: 23px; }
  .info { font-style: italic; font-weight: 300; font-size: 14.5px; line-height: 19px; background: var(--panel-dark); padding: 1px 6px; white-space: nowrap; }

  .bar { background: var(--label-red); color: #fff; font-weight: 600; font-size: 13.5px; height: 22px; line-height: 22px; text-align: center; }

  .reg-box { left: 73px; top: 299px; width: 503px; padding: 2px 0 3px; text-align: center; font-style: italic; font-weight: 300; font-size: 14px; line-height: 19px; background: var(--panel-dark); }

  .helmet-art { left: 574px; top: 103px; width: 170px; height: 312px; border-radius: 14px;
    background: linear-gradient(180deg, var(--art-mid) 0%, var(--art-dark) 100%); }
  .league-mark { left: 574px; top: 142px; width: 170px; text-align: center; font-weight: 600; font-size: 12px; color: #fff; letter-spacing: 1px; }

  .division-table { border-collapse: collapse; border: 2px solid var(--rule-light); background: var(--panel-dark); font-style: italic; table-layout: fixed; }
  .division-table td { border: 1.2px solid var(--rule-light); vertical-align: middle; }
  .division-table .group { width: 107px; font-weight: 400; font-size: 13.5px; line-height: 16px; padding: 0 5px; white-space: nowrap; }
  .division-table .weights { font-weight: 300; font-size: 12.3px; line-height: 13.5px; padding: 0 7px; white-space: nowrap; }
  .boys-table { left: 43px; top: 444px; width: 344px; }
  .boys-table tr { height: 32px; }
  .girls-table { left: 402px; top: 444px; width: 345px; }
  .girls-table .weights { font-size: 11.8px; padding: 0 4px; }

  .age-note { left: 88px; top: 682px; width: 607px; text-align: center; font-style: italic; font-weight: 300; font-size: 14px; line-height: 19px; background: var(--panel-dark); padding: 2px 0; }
  .weigh-list { left: 42px; top: 768px; width: 595px; font-style: italic; font-weight: 400; font-size: 14px; line-height: 20.5px; background: var(--panel-dark); padding: 3px 6px; white-space: nowrap; }
  .rules { left: 0; top: 850px; width: 784px; text-align: center; font-style: italic; font-weight: 300; font-size: 14px; line-height: 19px; }

  .contact { left: 38px; top: 1005px; font-weight: 600; font-size: 12.5px; line-height: 18.5px; }
  .contact .phone { letter-spacing: 2.4px; }
  .hotels { left: 534px; top: 1004px; font-style: italic; font-weight: 300; font-size: 14px; line-height: 19px; white-space: nowrap; }
</style>
</head>
<body>
<main class="flyer">
  <div class="flyer-texture" role="img" aria-label="Red weathered texture background"></div>

  <h1 class="abs title">
    <span class="title-num">7</span><span class="title-sup">TH</span>
    <span class="title-name">ANNUAL FALCON RIDGE CLASSIC</span>
  </h1>

  <div class="abs label" style="left:42px;top:122px;">Date:</div>
  <p class="abs info" style="left:42px;top:140px;">Saturday, January 25, 2025</p>

  <div class="abs label" style="left:329px;top:122px;">Location:</div>
  <p class="abs info" style="left:329px;top:140px;">Pinecrest Event Center<br>418 Harbor Blvd SW<br>Pinecrest, NC 27590</p>

  <div class="abs label" style="left:42px;top:198px;">Time:</div>
  <p class="abs info" style="left:42px;top:216px;">4U, 6U, 8U, 10U – Wrestling Starts at 8:30 am<br>12U, Middle School, &amp; High School – Wrestling Starts at 1:00 pm</p>

  <div class="abs bar" style="left:146px;top:270px;width:344px;">Register @ www.matbracket.com</div>

  <p class="abs reg-box">
    Early Registration $30.00 Deadline is January 19, 2025 at 11:59PM<br>
    Regular Registration $40.00 Deadline is January 22, 2025 at 11:59PM<br>
    Late Registration $50.00 Deadline is January 24, 2025 at 5:00PM<br>
    Registration is limited to the first 500 wrestlers<br>
    Non-CYGA Card Holders will pay an additional $5.00 at weigh-ins.
  </p>

  <div class="abs helmet-art" role="img" aria-label="Artwork area: dark warrior helmet illustration"></div>
  <p class="abs league-mark">CYGA</p>

  <div class="abs label label-wide" style="left:42px;top:410px;">Boys Divisions:</div>
  <div class="abs label label-wide" style="left:401px;top:410px;width:122px;">Girls Divisions:</div>

  <table class="abs division-table boys-table">
    <tr><td class="group">4 &amp; Under</td><td class="weights">30, 40, 50, HWT</td></tr>
    <tr><td class="group">6 &amp; Under</td><td class="weights">36, 40, 44, 48, 52, 56, 60, HWT</td></tr>
    <tr><td class="group">8 &amp; Under</td><td class="weights">40,44,48,52,56,60,64,68,72,<br>76,80,84,88,92, HWT</td></tr>
    <tr><td class="group">10 &amp; Under</td><td class="weights">52,56,60,64,68,72,76,80,84,<br>88,92,96,100,110, HWT</td></tr>
    <tr><td class="group">12 &amp; Under</td><td class="weights">64,68,72,76,80,84,88,92,96,100,<br>105,110,115,120,130,140,160, HWT</td></tr>
    <tr><td class="group">Middle School</td><td class="weights">72,76,80,88,92,96,100,105,110,115,<br>120,130,140,160,210, HWT</td></tr>
    <tr><td class="group">High School</td><td class="weights">106,113,120,126,132,138,144,150,157,<br>165,175,190,215, HWT</td></tr>
  </table>

  <table class="abs division-table girls-table">
    <tr style="height:38px;"><td class="group">K - 5</td><td class="weights">36,40,44,48,52,56,60,64,68,72,76,<br>80,84,88,92,96,100,110,120,HWT</td></tr>
    <tr style="height:42px;"><td class="group">Middle School</td><td class="weights">72,76,83,90,98,106,113,120,126,132,138,<br>145,152,160,170,182,190,220, HWT</td></tr>
    <tr style="height:41px;"><td class="group">Women's<br>High School</td><td class="weights">100,107,114,120,126,132,145,152,165,<br>185, HWT</td></tr>
  </table>

  <p class="abs age-note">*Age is based upon wrestler's age as of December 31, 2024.<br>Tournament director has the right to combine weight classes if deemed necessary.</p>

  <div class="abs label label-wide" style="left:42px;top:738px;">Weigh-ins:</div>
  <p class="abs weigh-list">
    January 24, 2025 5:00 pm to 7:00 pm (Early Weigh-ins - $10 cash due at scale)<br>
    January 25, 2025 6:00 am to 7:30 am (4U, 6U, 8U, 10U)<br>
    January 25, 2025 11:00 am to 12:00 pm (12 &amp; Under, MS, &amp; High School)
  </p>

  <p class="abs rules">
    Tenths are waived/dropped at weigh-ins. Satellite weigh-ins will not be allowed.<br>
    High School Divisions are given 2 lbs. growth allowance.<br>
    Custom medals will be given to the top 3 individual finishers in each bracket.<br>
    Custom Awards will be awarded to the top 4 teams. Referee decisions will be final.<br>
    Cedar Bend Athletics is not responsible for accidents, injuries, or theft during the tournament.
  </p>

  <div class="abs bar" style="left:220px;top:955px;width:344px;">Admission: $10.00 per person</div>

  <p class="abs contact">For More Information,<br>contact Tournament Director Dale Whitford:<br><span class="phone">2523814927</span></p>

  <p class="abs hotels">Hotels Available On-Site<br>Lakeside Suites (252)555-0140<br>Meadow Inn (252)555-0172<br>Harborview Lodge (252)555-0195</p>
</main>
</body>
</html>
```